Packaging design for Virgin Coconut Oil. 100% pure cold pressed coconut oil

We need a new packaging and label design for our Virgin Coconut Oil product. It is currently marketed in the Philippines as a food supplement. We would like to try marketing it to other Asian countries such as Singapore, Malaysia and Hong Kong. The company has been producing this product since 2004 but now would like to venture into exporting our products overseas.

Would like to see designs with earth, natural "organic" colors. Fresh, Clean and pure look. Our trade mark is "Kestrel Meadow". Its a 100% pure cold pressed virgin coconut oil. All in all, we want to totally repackage our product and re-design the trademark to cater to export markets. Thanks!

Mid to High

Health Product

cadf82
9bcb3b
33b8a4
ffffff
3176b5
3276b5
0592cd
fbed22
fece3e

• Bottle shape design ideas.

```html
<!DOCTYPE html>
<html lang="en">
<head>
<meta charset="utf-8">
<title>Kestrel Meadow Virgin Coconut Oil – Label</title>
<link rel="stylesheet" href="https://fonts.googleapis.com/css2?family=Montserrat:ital,wght@0,500;0,600;0,800;1,700&display=swap">
<style>
  :root {
    --label-light: #f2f6df;
    --label-mid: #e3edc7;
    --leaf-green: #6a9c3a;
    --title-green: #6b9e3b;
    --band-green: #5f9233;
    --tag-dark: #2b2b2b;
    --white: #ffffff;
    --coconut-a: #a9d163;
    --coconut-b: #7fb23a;
    --coconut-flesh: #f3e6d2;
  }
  * { box-sizing: border-box; margin: 0; padding: 0; }
  html, body {
    width: 1200px;
    height: 2239px;
    overflow: hidden;
    background: var(--label-light);
  }
  .label {
    position: relative;
    width: 1200px;
    height: 2239px;
    background: linear-gradient(160deg, var(--label-mid) 0%, var(--label-light) 45%, var(--label-light) 100%);
    font-family: "Montserrat", sans-serif;
    overflow: hidden;
  }
  .brand-ribbon {
    position: absolute;
    left: 393px;
    top: 0;
    width: 390px;
    height: 440px;
  }
  .brand-ribbon svg { position: absolute; inset: 0; }
  .brand-name {
    position: absolute;
    left: 0; right: 0;
    top: 130px;
    text-align: center;
    color: var(--white);
    font-weight: 500;
    font-size: 64px;
    line-height: 86px;
    text-transform: uppercase;
  }
  .product-title {
    position: absolute;
    left: 0; right: 0;
    top: 470px;
    text-align: center;
    color: var(--title-green);
    font-weight: 800;
    font-size: 204px;
    line-height: 232px;
    letter-spacing: -2px;
    text-transform: uppercase;
  }
  .coconut-art {
    position: absolute;
    left: 80px;
    top: 1210px;
    width: 1030px;
    height: 770px;
  }
  .claim-tag {
    position: absolute;
    left: 240px;
    top: 2032px;
    width: 720px;
    height: 74px;
  }
  .claim-tag svg { position: absolute; inset: 0; }
  .claim-text {
    position: relative;
    display: block;
    text-align: center;
    line-height: 74px;
    color: var(--white);
    font-style: italic;
    font-weight: 700;
    font-size: 46px;
  }
  .supplement-band {
    position: absolute;
    left: 0; right: 0;
    top: 2106px;
    height: 84px;
    background: var(--band-green);
    color: var(--white);
    text-align: center;
    font-weight: 600;
    font-size: 52px;
    line-height: 84px;
    text-transform: uppercase;
  }
</style>
</head>
<body>
  <main class="label">
    <div class="brand-ribbon">
      <svg width="390" height="440" viewBox="0 0 390 440" aria-hidden="true">
        <polygon points="0,0 390,0 390,420 195,360 0,420" fill="var(--leaf-green)"/>
      </svg>
      <div class="brand-name">Kestrel<br>Meadow</div>
    </div>

    <h1 class="product-title">Virgin<br>Coconut<br>Oil</h1>

    <svg class="coconut-art" viewBox="0 0 1030 770" role="img" aria-label="Photograph of fresh green coconuts, one cut in half showing white flesh">
      <defs>
        <radialGradient id="coconutGlow" cx="50%" cy="50%" r="55%">
          <stop offset="0%" stop-color="var(--coconut-a)"/>
          <stop offset="100%" stop-color="var(--coconut-b)" stop-opacity="0"/>
        </radialGradient>
      </defs>
      <ellipse cx="515" cy="400" rx="515" ry="370" fill="url(#coconutGlow)"/>
    </svg>

    <div class="claim-tag">
      <svg width="720" height="74" viewBox="0 0 720 74" aria-hidden="true">
        <polygon points="24,0 696,0 720,74 0,74" fill="var(--tag-dark)"/>
      </svg>
      <span class="claim-text">Approved Therapeutic Claim</span>
    </div>

    <div class="supplement-band">All Natural Food Supplement</div>
  </main>
</body>
</html>
```